Scale up packaging design for health & beauty product

New 2oz Lorquine Design Brief

I have an existing design for a beauty/health product in 1oz size that needs to be scaled up to a 2oz size.

Retail tube and packaging scale up - no original design required this job.

2 Parts to this Project

Part 1

Adobe Illustrator (ai) source files supplied with existing design on 1oz tube/box

Current files and design (from a previous selected winner) will be supplied.

The design is to be applied to 2oz template - provided for tube and box

Some minor word changes will be needed.

A final approved drug panel label will also be provided for tube and box to insert.

The product will be registered with the QMH in USA and needs what is called an NDC number. There is an area on the box (top right corner and back of drug panel) where this number (not yet available to me) will need to be inserted.

My company only receives the NDC number AFTER the design (from you) is submitted and approved - a fairly routine process

Once you finish the essential artwork/design/scaling on 2oz tube/box I will submit to get the NDC number, then come back to you and require you to insert in designated area for final approval before I get product made.

This submission for NDC could take a couple of weeks - not sure, hopefully sooner, a little patience necessary.

So a little back and forth will be required, with the minor changes in words etc.

Deliverables - Will be in AI (Adobe Illustrator) format and PDF for the 2D template.

Tube & Outer Box
Adobe Illustrator file (.ai) using supplied template for die lines prior to printing/manufacture.

**************************************************

Part 2

Once the 2D AI file is complete with the NDC then you can go ahead with the 3D images.

I will also need some excellent looking 3D images suitable for marketing. Examples will be supplied.

3D images to show the product and box and drug panel - suitable for high quality marketing.

I am also awaiting the final approval from manufacturer of what the cap on the tube will look like - once I have that then you can do the 3D rendering.

Deliverables - PNG files for 3D style renderings of front, back, side, and angled left and right, clear of any background, in high color and definition.

I have included a sampling of what I am after for the 3D renderings - I will need tube on its own, box on its own, tube coming out of box, different angles etc

****************************************************

Once satisfied with the 2D template work (prior to sending for NDC number I will make a partial payment of 50% - the remainder to be paid upon final completion of all work.

A previous designer here failed to respond to my emails after initial design so as to get the NDC number

If this is a hassle free job with you I have another job (very similar) to do immediately as well.

But this project first.

Industry/Entity Type

Health Product

Font styles to use
Sans Serif

Requirements
Must have
• Clear neat work suitable for commercial application
• Be able to accept that the project may take a couple of weeks because of the NDC number
Nice to have
• Clear concise understanding of work
• Be able to respond quickly to any changes required

```html
<!DOCTYPE html>
<html lang="en">
<head>
<meta charset="utf-8">
<title>Lorquine Numb – Lidocaine 4% Tube Dieline</title>
<link href="https://fonts.googleapis.com/css2?family=Open+Sans:wght@400;600;700&family=Source+Sans+3:wght@400;600;700&family=PT+Sans:wght@700&display=swap" rel="stylesheet">
<style>
  :root{
    --ink:#1a1a1a;
    --panel-dark:#151515;
    --panel-light:#ffffff;
    --brand-orange:#f26a21;
    --white:#ffffff;
    --note-red:#e8262b;
    --note-pink:#e23a6a;
    --note-grey:#555555;
    --note-faint:#cfcfcf;
    --rule-grey:#c9c9c9;
    --facts-text:#4a4a4a;
  }
  *{box-sizing:border-box;margin:0;padding:0}
  html,body{width:1200px;height:1000px;overflow:hidden;background:var(--white)}
  .canvas{position:relative;width:1200px;height:1000px;overflow:hidden;background:var(--white);font-family:"Open Sans",Arial,sans-serif;color:var(--ink)}
  .abs{position:absolute}

  /* annotations */
  .direction-note{left:300px;top:4px;width:340px;text-align:center;color:var(--note-red);font-family:"Source Sans 3",sans-serif;font-size:22px;line-height:28px;letter-spacing:.3px}
  .width-label{left:388px;top:80px;font-size:40px;font-weight:400;color:var(--ink)}
  .edge-label{font-family:"PT Sans",sans-serif;font-weight:700;font-size:15px;color:var(--ink);writing-mode:vertical-rl;letter-spacing:1px}
  .cap-end{left:28px;top:172px}
  .open-end{left:890px;top:170px}
  .center-line{left:852px;top:300px;font-size:11px;color:var(--note-grey);writing-mode:vertical-rl;font-weight:700;font-family:"PT Sans",sans-serif;line-height:13px}
  .front-label{left:915px;top:330px;font-size:21px;color:#8a8a8a}
  .height-label{left:52px;top:480px;font-size:22px;color:var(--ink)}
  .half-label{left:740px;top:487px;font-size:21px;color:#d5d5d5}
  .gap-label{left:796px;top:165px;font-size:20px;color:var(--ink)}
  .slot-label{left:719px;top:199px;font-size:14px;color:var(--ink)}
  .margin-label{left:158px;top:852px;font-size:17px;color:var(--note-faint)}
  .approval-note{left:0;top:912px;width:822px;text-align:center;font-size:28px;line-height:42px;color:var(--note-faint)}

  /* tube panel */
  .tube-panel{left:170px;top:170px;width:553px;height:635px;background:linear-gradient(180deg,var(--panel-dark) 0%,#262626 30%,#9a9a9a 60%,#f4f4f4 78%,var(--panel-light) 100%)}
  .feather-art{left:330px;top:195px;width:380px;height:150px;border-radius:60px;background:radial-gradient(ellipse at 60% 50%,rgba(120,120,120,.35),rgba(60,60,60,0) 70%)}
  .brand{left:355px;top:202px;display:flex;align-items:center;gap:8px}
  .brand-dot{width:16px;height:16px;background:var(--brand-orange)}
  .brand-name{font-family:"PT Sans",sans-serif;font-weight:700;font-size:28px;color:var(--brand-orange);letter-spacing:.5px}
  .claim{left:390px;width:240px;text-align:center;font-family:"PT Sans",sans-serif;font-weight:700;color:var(--white)}
  .claim-small{font-size:11px;line-height:15px;top:236px}
  .claim-uses{top:267px;font-size:18px;letter-spacing:.4px}
  .descriptor{left:222px;top:368px;font-family:"Source Sans 3",sans-serif;font-size:21px;color:var(--white)}
  .product-name{left:218px;top:388px;font-family:"Source Sans 3",sans-serif;font-size:52px;font-weight:400;color:var(--white);letter-spacing:.5px}
  .net-wt{left:472px;top:458px;font-family:"PT Sans",sans-serif;font-weight:700;font-size:13px;color:var(--white)}

  /* drug facts */
  .facts{top:490px;height:295px;border:1px solid var(--rule-grey);background:rgba(255,255,255,.55);font-family:"Source Sans 3",sans-serif;font-size:8.6px;line-height:10.2px;color:var(--facts-text);padding:0 4px}
  .facts-left{left:202px;width:226px}
  .facts-right{left:432px;width:206px}
  .facts h3{font-size:11px;font-weight:600;color:#666;border-bottom:1px solid var(--rule-grey);margin:0 -4px 2px;padding:1px 4px}
  .facts h3 small{font-size:7px;font-weight:400}
  .facts h4{font-size:9.5px;font-weight:400;color:#555;margin-top:3px;border-top:1px solid var(--rule-grey);padding-top:2px}
  .facts .row{display:flex;justify-content:space-between}
  .facts .bx::before{content:"■";font-size:6px;margin-right:1px}
</style>
</head>
<body>
<div class="canvas">

  <svg class="abs" style="left:0;top:0" width="1200" height="1000" aria-hidden="true">
    <g stroke="#e8262b" stroke-width="2" fill="#e8262b">
      <line x1="298" y1="62" x2="298" y2="14"/><polygon points="291,18 298,2 305,18"/>
      <line x1="638" y1="62" x2="638" y2="14"/><polygon points="631,18 638,2 645,18"/>
    </g>
    <g stroke="#333" stroke-width="1" fill="none">
      <line x1="165" y1="133" x2="722" y2="133"/>
      <line x1="165" y1="118" x2="165" y2="148"/><line x1="722" y1="118" x2="722" y2="148"/>
      <line x1="112" y1="170" x2="112" y2="805"/>
      <line x1="82" y1="170" x2="162" y2="170"/><line x1="72" y1="805" x2="162" y2="805"/>
      <line x1="738" y1="170" x2="790" y2="170"/><line x1="738" y1="185" x2="790" y2="185"/>
    </g>
    <g stroke="#e23a6a" stroke-width="1">
      <line x1="95" y1="345" x2="101" y2="345"/><line x1="95" y1="663" x2="101" y2="663"/>
      <line x1="773" y1="345" x2="773" y2="470"/><line x1="815" y1="345" x2="820" y2="345"/>
    </g>
    <g stroke="#e6e6e6"><line x1="168" y1="812" x2="168" y2="848"/><line x1="192" y1="812" x2="192" y2="848"/></g>
  </svg>

  <div class="abs direction-note">ARTWORK DIRECTION.<br>DO NOT CHANGE.</div>
  <div class="abs width-label">95mm</div>
  <div class="abs edge-label cap-end">CAP END</div>
  <div class="abs edge-label open-end">OPEN END</div>
  <div class="abs center-line">CENTER LINE<br>PANEL 1</div>
  <div class="abs front-label">FORNT</div>
  <div class="abs height-label">109.9mm</div>
  <div class="abs gap-label">3mm</div>
  <div class="abs slot-label">8x2mm</div>

  <div class="abs tube-panel"></div>
  <div class="abs feather-art" role="img" aria-label="Faint grey feather decoration"></div>

  <div class="abs brand"><span class="brand-dot"></span><span class="brand-name">Lorquine® Numb</span></div>
  <div class="abs claim claim-small">4% Lidocaine Cream<br>Pain Relief Numbing Cream For:</div>
  <div class="abs claim claim-uses">Tattoos - Waxing - Laser</div>

  <div class="abs descriptor">Pain Relieving Cream</div>
  <div class="abs product-name">Lidocaine 4%</div>
  <div class="abs net-wt">NET WT. 2.0 Oz. (56.7g)</div>
  <div class="abs half-label">54.95mm</div>

  <section class="abs facts facts-left">
    <h3>Drug Facts</h3>
    <div class="row"><span style="font-size:10px">Active ingredient</span><span style="font-size:10px">Purpose</span></div>
    <div class="row"><span>Lidocaine 4%.........................</span><span>Topical analgesic</span></div>
    <h4>Use</h4>
    <p>for temporary relief of pain associated with:</p>
    <p><span class="bx">minor burns</span> <span class="bx">sunburn</span> <span class="bx">minor cuts</span> <span class="bx">scrapes</span></p>
    <p><span class="bx">insect bites</span> <span class="bx">minor skin irritations</span></p>
    <h4>Warnings</h4>
    <p>For external use only.</p>
    <p style="margin-top:3px">Do not use</p>
    <p class="bx">on large areas of the body</p>
    <p class="bx">on broken, blistered, or oozing skin</p>
    <p class="bx">on deep or puncture wounds</p>
    <p class="bx">for more than one week without consulting a doctor</p>
    <p class="bx">if seal on tube is punctured or missing</p>
    <p>When using this product <span class="bx">avoid contact with eyes</span></p>
    <p style="margin-top:3px">Stop use and ask a doctor if</p>
    <p class="bx">condition worsens</p>
    <p class="bx">symptoms persist for more than 7 days</p>
    <p class="bx">condition clears up and returns</p>
    <p>If pregnant or breast-feeding, ask a health professional before use.</p>
    <p>Keep out of reach of children.</p>
  </section>

  <section class="abs facts facts-right">
    <h3>Drug Facts <small>(continued)</small></h3>
    <p style="font-size:9.5px">Directions</p>
    <p>Adults and children 2 years old and older</p>
    <p class="bx">clean the affected area</p>
    <p class="bx">apply a thin layer of product to affected area</p>
    <p>&nbsp;&nbsp;every 6 to 8 hours up to 3 times every 24 hours</p>
    <p>Children under 2 years old</p>
    <p>Consult a doctor</p>
    <h4>Other information</h4>
    <p class="bx">store at 15° to 30°C (59° to 86°F)</p>
    <p class="bx">do not use if tube seal is broken</p>
    <h4>Inactive ingredients</h4>
    <p>aloe vera, benzyl alcohol, carbomer, glycerin, water</p>
  </section>

  <div class="abs margin-label">5mm</div>
  <div class="abs approval-note">VERDALIN APPROVED DIELINE AND COPY<br>FOR LIDOCAINE 4% TUBE</div>
</div>
</body>
</html>
```